TBV business card

For a business card with our logo

Contact Information for Business Card

Lucien MARVET
Founder & CEO
email : ceo@brightlanternstudio.com / www.brightlanternstudio.com /
instagram / facebook / WhatsApp
N°: +590 690 482 517

Colors

Designer to choose colors to be used in the design.

```html
<!DOCTYPE html>
<html lang="en">
<head>
<meta charset="utf-8">
<title>TBV business card</title>
<link rel="stylesheet" href="https://fonts.googleapis.com/css2?family=Lato:wght@400;700&display=swap">
<style>
  :root {
    --backdrop: #7a5c3e;
    --card: #07080b;
    --brand-blue: #1f5fb0;
    --brand-orange: #f07a26;
    --muted: #6d6e70;
    --ghost: #1c1d20;
  }
  * { margin: 0; padding: 0; box-sizing: border-box; }
  html, body { width: 1200px; height: 1023px; overflow: hidden; }
  body {
    background: var(--backdrop);
    font-family: "Lato", sans-serif;
    position: relative;
  }
  .card {
    position: absolute;
    left: 248px;
    width: 681px;
    height: 390px;
    background: var(--card);
    overflow: hidden;
  }
  .card--front { top: 87px; }
  .card--back { top: 542px; height: 388px; }

  /* brand mark: plain circle + name */
  .brand { position: absolute; text-align: center; }
  .brand__dot { display: block; margin: 0 auto; border-radius: 50%; background: var(--brand-orange); }
  .brand__name {
    display: block;
    color: var(--brand-blue);
    font-weight: 700;
    letter-spacing: 0.04em;
    line-height: 1.1;
    text-transform: uppercase;
  }

  .card--front .brand { left: 62px; top: 112px; width: 260px; }
  .card--front .brand__dot { width: 96px; height: 96px; margin-bottom: 14px; }
  .card--front .brand__name { font-size: 24px; }

  .divider {
    position: absolute;
    left: 334px; top: 113px;
    width: 1px; height: 153px;
    background: var(--brand-blue);
  }
  .person { position: absolute; left: 353px; top: 108px; }
  .person__name { font-size: 30px; font-weight: 700; color: var(--brand-blue); line-height: 1.1; }
  .person__role { font-size: 17px; color: var(--muted); margin-top: 2px; }

  .contacts { position: absolute; left: 359px; top: 182px; list-style: none; }
  .contacts li {
    display: flex; align-items: center;
    height: 31.5px;
    font-size: 17px; color: var(--muted);
  }
  .contacts svg { width: 16px; height: 16px; margin-right: 12px; flex: none; }

  .card--back .ghost-field {
    position: absolute; left: 0; top: 60px; width: 681px; height: 220px;
    background: linear-gradient(100deg, rgba(40,41,45,0.55), rgba(20,21,24,0.2) 50%, rgba(40,41,45,0.5));
  }
  .card--back .brand { left: 140px; top: 55px; width: 400px; }
  .card--back .brand__dot { width: 152px; height: 152px; margin-bottom: 22px; }
  .card--back .brand__name { font-size: 34px; }

  .socials { position: absolute; left: 296px; top: 340px; display: flex; gap: 9px; }
  .socials span { width: 24px; height: 24px; border-radius: 4px; background: var(--brand-orange); }
</style>
</head>
<body>

<section class="card card--front">
  <div class="brand">
    <span class="brand__dot"></span>
    <span class="brand__name">Bright Lantern<br>Studio</span>
  </div>
  <div class="divider"></div>
  <div class="person">
    <div class="person__name">Lucien MARVET</div>
    <div class="person__role">Founder &amp; CEO</div>
  </div>
  <ul class="contacts">
    <li>
      <svg viewBox="0 0 24 24" fill="var(--brand-blue)"><path d="M6.6 10.8a15 15 0 0 0 6.6 6.6l2.2-2.2c.3-.3.7-.4 1-.2 1.1.4 2.3.6 3.6.6.6 0 1 .4 1 1V20c0 .6-.4 1-1 1A17 17 0 0 1 3 4c0-.6.4-1 1-1h3.5c.6 0 1 .4 1 1 0 1.3.2 2.5.6 3.6.1.3 0 .7-.2 1z"/></svg>
      +590 690 482 517
    </li>
    <li>
      <svg viewBox="0 0 24 24" fill="var(--brand-blue)"><path d="M2 5h20v14H2z"/><path d="M2 5l10 8 10-8" fill="none" stroke="var(--card)" stroke-width="2"/></svg>
      ceo@brightlanternstudio.com
    </li>
    <li>
      <svg viewBox="0 0 24 24" fill="none" stroke="var(--brand-blue)" stroke-width="2"><circle cx="12" cy="12" r="10"/><path d="M2 12h20M12 2c3 3 3 17 0 20M12 2c-3 3-3 17 0 20"/></svg>
      www.brightlanternstudio.com
    </li>
  </ul>
</section>

<section class="card card--back">
  <div class="ghost-field" role="img" aria-label="Faint scattered square pattern behind the brand mark"></div>
  <div class="brand">
    <span class="brand__dot"></span>
    <span class="brand__name">Bright Lantern<br>Studio</span>
  </div>
  <div class="socials" aria-label="Social profiles">
    <span></span><span></span><span></span>
  </div>
</section>

</body>
</html>
```